Business Card Design Project for - The Hollowmere Planting Company Ltd. We are a Landscape and garden

I would like designer to use all special glosses etc so i can have a professional looking business card. The theme of the business card can reflect that of the Logo attached by MarkQuarry or your own unique ideas.. please feel free to go wild as i hope i can select a winner i like - my budget will be committed so please get involved. Good luck and thank you Rowan

Target Market(s)

Must look Professional

General Public and Businesses including Councils, Local Government, Hospitals, Hotels, Professionals and Professional Sports People.

Industry/Entity Type

Landscape Gardening

Contact Information for Business Card

The Hollowmere Planting Company Ltd

Mr R.T Pelling
Head Office - Quayside Works Manchester
t. 0784 529 618
e. info@hollowmereplanting.co.uk
w. www.hollowmereplanting.co.uk

Facebook - https://www.friendpage.example/TheHollowmerePlantingCompany/
Twitter - https://chirpline.example/TheMossyTrowel
Instagram - https://www.snapgrid.example/thehollowmereplantingcompany/?hl=en
Google+ - https://circles.searchhub.example/u/0/208475639102847561932
Yelp - https://www.reviewden.example/biz/the-hollowmere-planting-company-manchester-4

Font styles to use
Serif
Script
Other font styles liked:
• I don't have much of an idea of font types sorry

Colors

Designer to choose colors to be used in the design.

Requirements
Must have
• A Professional look and Design
• Special effects with gloss and fading of colours possibly..
• Front and back design
Nice to have
• All special features with effects and gloss etc

```html
<!DOCTYPE html>
<html lang="en">
<head>
<meta charset="utf-8">
<title>The Hollowmere Planting Company Ltd – Business Card</title>
<link rel="stylesheet" href="https://fonts.googleapis.com/css2?family=Cinzel:wght@400&family=Montserrat:wght@400;500&display=swap">
<style>
  :root {
    --backdrop: #1d1d1f;
    --card: #2a2a2b;
    --card-edge: #333335;
    --ink-light: #f2f2f2;
    --ink-muted: #a3a3a5;
    --ink-grey: #8e8e90;
    --green: #3fbf35;
    --green-deep: #1f8a25;
    --rule: #d9d9d9;
  }
  * { margin: 0; padding: 0; box-sizing: border-box; }
  html, body { width: 1200px; height: 1200px; overflow: hidden; background: var(--backdrop); }
  .canvas {
    width: 1200px; height: 1200px;
    display: flex; flex-direction: column; align-items: center; justify-content: center; gap: 60px;
  }
  .card {
    position: relative;
    width: 840px; height: 480px;
    background: radial-gradient(ellipse at 30% 20%, #303032 0%, var(--card) 60%, #252526 100%);
    border: 1px solid var(--card-edge);
    box-shadow: 0 20px 40px rgba(0,0,0,0.45);
  }

  /* Front */
  .front { display: flex; flex-direction: column; align-items: center; justify-content: center; gap: 34px; }
  .brand-dot {
    width: 96px; height: 96px; border-radius: 50%;
    background: radial-gradient(circle at 35% 30%, #7be35a 0%, var(--green) 45%, var(--green-deep) 100%);
  }
  .brand-name {
    font-family: "Cinzel", serif; font-weight: 400;
    color: var(--ink-grey); text-align: center;
    font-size: 34px; letter-spacing: 3px; line-height: 1.35;
  }

  /* Back */
  .back { font-family: "Montserrat", sans-serif; }
  .holder { position: absolute; left: 56px; top: 62px; }
  .holder-name { color: var(--ink-light); font-size: 34px; font-weight: 400; letter-spacing: 1px; }
  .holder-role { color: var(--green); font-size: 14px; font-weight: 500; letter-spacing: 0.5px; margin-top: 6px; }

  .rule { position: absolute; height: 2px; background: var(--rule); }
  .rule.contact-top { left: 40px; width: 380px; top: 278px; }
  .rule.contact-bottom { left: 40px; width: 380px; top: 420px; }
  .rule.social-top { left: 420px; width: 380px; top: 150px; }
  .rule.social-bottom { left: 420px; width: 380px; top: 330px; }
  .rule.divider { left: 418px; width: 2px; top: 150px; height: 270px; }

  .list { position: absolute; list-style: none; color: var(--ink-light); font-size: 15px; }
  .list li { display: flex; align-items: center; gap: 12px; height: 27px; }
  .contacts { left: 56px; top: 300px; }
  .socials { left: 440px; top: 170px; }
  .icon { width: 16px; height: 16px; flex: none; }
  .social-dot { width: 13px; height: 13px; border-radius: 50%; background: var(--green); flex: none; }
</style>
</head>
<body>
<main class="canvas">

  <section class="card front" aria-label="Card front">
    <span class="brand-dot" aria-hidden="true"></span>
    <h1 class="brand-name">The Hollowmere Planting<br>Company Ltd</h1>
  </section>

  <section class="card back" aria-label="Card back">
    <div class="holder">
      <p class="holder-name">MR R.T PELLING</p>
      <p class="holder-role">HEAD OFFICE - QUAYSIDE WORKS MANCHESTER</p>
    </div>

    <span class="rule social-top"></span>
    <span class="rule social-bottom"></span>
    <span class="rule contact-top"></span>
    <span class="rule contact-bottom"></span>
    <span class="rule divider"></span>

    <ul class="list socials">
      <li><span class="social-dot"></span>TheHollowmerePlantingCompany</li>
      <li><span class="social-dot"></span>TheMossyTrowel</li>
      <li><span class="social-dot"></span>thehollowmereplantingcompany</li>
      <li><span class="social-dot"></span>The Hollowmere Planting Company</li>
      <li><span class="social-dot"></span>The Hollowmere Planting Company</li>
    </ul>

    <ul class="list contacts">
      <li>
        <svg class="icon" viewBox="0 0 16 16" aria-hidden="true"><path d="M3.5 1.5l2.5 0 1 3.5-1.8 1.2a8 8 0 0 0 4.6 4.6L11 9l3.5 1v2.5c0 1-1 2-2 2C6.5 14.5 1.5 9.5 1.5 3.5c0-1 1-2 2-2z" fill="var(--green)"/></svg>
        0784 529 618
      </li>
      <li>
        <svg class="icon" viewBox="0 0 16 16" aria-hidden="true"><rect x="1.5" y="3.5" width="13" height="9" rx="1" fill="var(--green)"/><path d="M2 4.5l6 4.5 6-4.5" stroke="var(--card)" stroke-width="1.4" fill="none"/></svg>
        info@hollowmereplanting.co.uk
      </li>
      <li>
        <svg class="icon" viewBox="0 0 16 16" aria-hidden="true"><circle cx="8" cy="8" r="6.5" fill="none" stroke="var(--green)" stroke-width="1.6"/><path d="M1.5 8h13M8 1.5c-3 3.5-3 9.5 0 13M8 1.5c3 3.5 3 9.5 0 13" stroke="var(--green)" stroke-width="1.2" fill="none"/></svg>
        www.hollowmereplanting.co.uk
      </li>
    </ul>
  </section>

</main>
</body>
</html>
```